BOLT Banner Ads for businesses who are keeping up with NRB guidelines

Banner ads - banner ad templates for us to advertise. We need this to be available in all of the key sizes for pomvia adlines and VS. Keep in mind, I want the template so we can adjust the wording. Sample wording is below:
NRB Compliant; BOLT Certified
Worried about COVID 19? Visit BOLT Certified Businesses
Protect you and your family, go to BOLT Certified Businesses
We are BOLT Certified, come see us today!
BOLT Certified businesses; giving you confidence
Be Confident with a BOLT Certification

Please feel free to check out our other contests for a better sense of the look and feel:
https://jobs.crewmosaic.com/job/5162078
https://jobs.crewmosaic.com/job/5162391

Target Market(s)

These ads are aimed at the general public to announce the certification.

Requirements
Must have
• We need the different banner sizes for pomvia adlines, vexaspot marketing, etc.

```html
<!DOCTYPE html>
<html lang="en">
<head>
<meta charset="utf-8">
<title>BOLT Banner Ads</title>
<link rel="stylesheet" href="https://fonts.googleapis.com/css2?family=Poppins:wght@400;500;700&display=swap">
<style>
  :root {
    --board-dark: #040d1c;
    --board-mid: #0b1f3d;
    --brand-blue: #0a65b4;
    --brand-navy: #17386a;
    --brand-dot: #2a8fd4;
    --paper: #ffffff;
    --paper-shade: #ececec;
    --photo-light: #e9e9e9;
    --photo-dark: #b9b9b9;
    --title-grey: #d9d9d9;
    --text-white: #ffffff;
  }
  * { box-sizing: border-box; margin: 0; padding: 0; }
  html, body { width: 1200px; height: 970px; overflow: hidden; }
  body {
    position: relative;
    font-family: "Poppins", sans-serif;
    background: radial-gradient(ellipse at 75% 70%, #12284a 0%, var(--board-mid) 35%, var(--board-dark) 80%);
  }
  .banner {
    position: absolute;
    background: linear-gradient(125deg, var(--paper) 0%, var(--paper) 55%, var(--paper-shade) 100%);
    overflow: hidden;
  }
  .banner svg.shape { position: absolute; inset: 0; }
  .photo {
    position: absolute;
    background: linear-gradient(160deg, var(--photo-light) 0%, var(--photo-dark) 100%);
  }
  .logo {
    position: absolute;
    display: flex;
    align-items: center;
    gap: 5px;
    color: var(--brand-navy);
    font-weight: 400;
    line-height: 1;
  }
  .logo-dot { border-radius: 50%; background: var(--brand-dot); flex: none; }
  .copy { position: absolute; color: var(--text-white); line-height: 1.1; }
  .copy .lead { font-weight: 400; display: block; }
  .copy .headline { font-weight: 700; display: block; }
  .copy .cta { font-weight: 500; display: block; }

  .board-logo { position: absolute; left: 966px; top: 96px; display: flex; align-items: center; gap: 8px; color: var(--text-white); font-size: 32px; font-weight: 400; }
  .board-logo .logo-dot { width: 26px; height: 26px; background: var(--text-white); }

  .board-title { position: absolute; left: 110px; top: 771px; color: var(--title-grey); font-size: 34px; font-weight: 700; }
  .board-text { position: absolute; left: 110px; top: 824px; width: 370px; color: var(--text-white); font-size: 11.5px; line-height: 1.5; }
</style>
</head>
<body>

<div class="board-logo"><span class="logo-dot"></span>BOLT</div>

<!-- Skyscraper 111 x 555 -->
<section class="banner" style="left:108px;top:132px;width:111px;height:555px;">
  <div class="photo" role="img" aria-label="Doctor in face mask and white coat with stethoscope" style="left:0;top:85px;width:111px;height:260px;"></div>
  <svg class="shape" width="111" height="555" viewBox="0 0 111 555"><polygon points="0,300 111,349 111,555 0,555" fill="var(--brand-blue)"/></svg>
  <div class="logo" style="left:14px;top:46px;font-size:20px;"><span class="logo-dot" style="width:14px;height:14px;"></span>BOLT</div>
  <div class="copy" style="left:10px;top:428px;">
    <span class="lead" style="font-size:12px;">Worried about</span>
    <span class="headline" style="font-size:18px;margin-top:2px;">COVID 19?</span>
    <span class="cta" style="font-size:10px;margin-top:8px;line-height:1.25;">Visit BOLT Certified<br>Businesses</span>
  </div>
</section>

<!-- Small leaderboard 433 x 55 -->
<section class="banner" style="left:248px;top:132px;width:433px;height:55px;">
  <div class="photo" role="img" aria-label="Woman sneezing into a tissue" style="left:120px;top:0;width:90px;height:55px;"></div>
  <svg class="shape" width="433" height="55" viewBox="0 0 433 55"><polygon points="233,0 433,0 433,55 187,55" fill="var(--brand-blue)"/></svg>
  <div class="logo" style="left:14px;top:19px;font-size:16px;"><span class="logo-dot" style="width:12px;height:12px;"></span>BOLT</div>
  <div class="copy" style="left:239px;top:13px;">
    <span style="font-size:13px;font-weight:400;">Worried about </span><span style="font-size:16px;font-weight:700;">COVID 19?</span>
    <span class="cta" style="font-size:8px;margin-top:1px;">Visit BOLT Certified Businesses</span>
  </div>
</section>

<!-- Leaderboard 667 x 83 -->
<section class="banner" style="left:248px;top:214px;width:667px;height:83px;">
  <div class="photo" role="img" aria-label="Woman wearing a surgical mask" style="left:210px;top:0;width:160px;height:83px;"></div>
  <svg class="shape" width="667" height="83" viewBox="0 0 667 83"><polygon points="373,0 667,0 667,83 302,83" fill="var(--brand-blue)"/></svg>
  <div class="logo" style="left:28px;top:28px;font-size:24px;"><span class="logo-dot" style="width:18px;height:18px;"></span>BOLT</div>
  <div class="copy" style="left:389px;top:20px;">
    <span style="font-size:18px;font-weight:400;">Worried about </span><span style="font-size:23px;font-weight:700;">COVID 19?</span>
    <span class="cta" style="font-size:12px;margin-top:3px;margin-left:6px;">Visit BOLT Certified Businesses</span>
  </div>
</section>

<!-- Medium rectangle 277 x 231 -->
<section class="banner" style="left:248px;top:323px;width:277px;height:231px;">
  <div class="photo" role="img" aria-label="Woman wearing a respirator mask" style="left:150px;top:0;width:127px;height:150px;"></div>
  <svg class="shape" width="277" height="231" viewBox="0 0 277 231"><polygon points="0,66 277,184 277,231 0,231" fill="var(--brand-blue)"/></svg>
  <div class="logo" style="left:33px;top:33px;font-size:22px;"><span class="logo-dot" style="width:16px;height:16px;"></span>BOLT</div>
  <div class="copy" style="left:26px;top:135px;">
    <span class="lead" style="font-size:17px;">Worried about</span>
    <span class="headline" style="font-size:27px;">COVID 19?</span>
    <span class="cta" style="font-size:11px;margin-top:8px;">Visit BOLT Certified Businesses</span>
  </div>
</section>

<!-- Half page tall 277 x 555 -->
<section class="banner" style="left:598px;top:323px;width:277px;height:555px;">
  <div class="photo" role="img" aria-label="Doctor in face mask and glasses putting on gloves" style="left:60px;top:100px;width:217px;height:330px;"></div>
  <svg class="shape" width="277" height="555" viewBox="0 0 277 555"><polygon points="0,298 277,417 277,555 0,555" fill="var(--brand-blue)"/></svg>
  <div class="logo" style="left:30px;top:42px;font-size:34px;"><span class="logo-dot" style="width:24px;height:24px;"></span>BOLT</div>
  <div class="copy" style="left:27px;top:424px;">
    <span class="lead" style="font-size:22px;">Worried about</span>
    <span class="headline" style="font-size:35px;">COVID 19?</span>
    <span class="cta" style="font-size:14.5px;margin-top:9px;">Visit BOLT Certified Businesses</span>
  </div>
</section>

<!-- Wide skyscraper 148 x 555 -->
<section class="banner" style="left:940px;top:214px;width:148px;height:555px;">
  <div class="photo" role="img" aria-label="Doctor in face mask and glasses with stethoscope" style="left:0;top:100px;width:148px;height:260px;"></div>
  <svg class="shape" width="148" height="555" viewBox="0 0 148 555"><polygon points="0,311 148,375 148,555 0,555" fill="var(--brand-blue)"/></svg>
  <div class="logo" style="left:16px;top:42px;font-size:22px;"><span class="logo-dot" style="width:15px;height:15px;"></span>BOLT</div>
  <div class="copy" style="left:15px;top:412px;">
    <span class="lead" style="font-size:15.5px;">Worried about</span>
    <span class="headline" style="font-size:25px;">COVID 19?</span>
    <span class="cta" style="font-size:13px;margin-top:7px;line-height:1.25;">Visit BOLT Certified<br>Businesses</span>
  </div>
</section>

<h1 class="board-title">BOLT Banner Ads</h1>
<p class="board-text">Contrary to popular belief, Lorem Ipsum is not simply random text. It has roots in a piece of classical Latin literature from 45 BC, making it over 2000 years old.</p>

</body>
</html>
```